Brightstone Roofing Business Card

This is my current business card. But I’d like to make some changes. Somewhere on the card I’d like to list some of the services we offer. Maybe on the back? But I’d still like to keep the red. White and black modern look.

-residential & commercial roofing
-Roof Repairs & Maintenance
-Storm Damage & Insurance Claims specialist
-Christmas Lights and permanent Christmas lights
Fencing. Windows. Gutters. Siding. Sheetrock, painting.

```html
<!DOCTYPE html>
<html lang="en">
<head>
<meta charset="utf-8">
<title>Brightstone Roofing Co. — Business Card</title>
<link rel="stylesheet" href="https://fonts.googleapis.com/css2?family=Montserrat:wght@700;800&family=Lato:wght@300;400&family=Oswald:wght@400&display=swap">
<style>
  :root {
    --stage: #222326;
    --card-white: #ffffff;
    --card-black: #131316;
    --ink: #141414;
    --red: #e3101b;
    --red-deep: #8e0a10;
    --grey: #6d6d6d;
    --rule: #e1e1e1;
  }
  * { margin: 0; padding: 0; box-sizing: border-box; }
  html, body { width: 1200px; height: 952px; overflow: hidden; }
  body { background: var(--stage); position: relative; font-family: "Lato", sans-serif; }

  .card {
    position: absolute;
    left: 290px;
    width: 620px;
    height: 354px;
    overflow: hidden;
    box-shadow: 0 10px 30px rgba(0,0,0,.45);
  }
  .card--front { top: 92px; background: var(--card-white); }
  .card--back { top: 506px; background: var(--card-black); }

  /* Front */
  .edge-bar { position: absolute; width: 16px; background: var(--ink); }
  .edge-bar--top { left: 0; top: 0; height: 150px; }
  .edge-bar--bottom { right: 0; bottom: 0; height: 150px; }

  .brand {
    position: absolute;
    display: flex;
    flex-direction: column;
    align-items: center;
    gap: 12px;
  }
  .card--front .brand { left: 70px; top: 92px; width: 200px; }
  .brand__dot { width: 66px; height: 66px; border-radius: 50%; background: var(--red); }
  .brand__name {
    font-family: "Montserrat", sans-serif;
    font-weight: 800;
    color: var(--red);
    text-align: center;
    line-height: 1.1;
    letter-spacing: 1px;
  }
  .card--front .brand__name { font-size: 21px; }

  .divider {
    position: absolute;
    left: 318px; top: 60px;
    width: 1px; height: 234px;
    background: var(--rule);
  }

  .person { position: absolute; left: 352px; top: 108px; }
  .person__name {
    font-family: "Montserrat", sans-serif;
    font-weight: 700;
    font-size: 26px;
    letter-spacing: 2px;
    color: var(--ink);
  }
  .person__name .accent { color: var(--red); }
  .person__role {
    font-weight: 300;
    font-size: 15px;
    letter-spacing: 2px;
    color: var(--grey);
    margin-top: 2px;
  }
  .contacts { list-style: none; margin-top: 16px; }
  .contacts li {
    display: flex; align-items: center; gap: 8px;
    font-size: 14px; color: var(--grey); line-height: 22px;
  }
  .contacts svg { width: 13px; height: 13px; fill: var(--red); flex: none; }

  /* Back */
  .mascot-area {
    position: absolute; left: 0; top: 0;
    width: 250px; height: 100%;
    background: radial-gradient(circle at 45% 45%, var(--red) 0%, var(--red-deep) 55%, var(--card-black) 100%);
  }
  .services {
    position: absolute; left: 290px; top: 40px;
    list-style: none;
    font-family: "Oswald", sans-serif;
    font-size: 16px; color: #fff; line-height: 27px;
  }
  .services li::before,
  .services .pair span::before {
    content: "";
    display: inline-block;
    width: 5px; height: 5px; border-radius: 50%;
    background: var(--red);
    margin-right: 7px;
    vertical-align: middle;
  }
  .services .pair::before { display: none; }
  .services .pair span { margin-right: 16px; }
  .card--back .brand { left: 290px; top: 258px; align-items: flex-start; }
  .card--back .brand__name { font-size: 24px; text-align: left; }
</style>
</head>
<body>

<section class="card card--front" aria-label="Business card front">
  <div class="edge-bar edge-bar--top"></div>
  <div class="edge-bar edge-bar--bottom"></div>

  <div class="brand">
    <div class="brand__dot"></div>
    <p class="brand__name">BRIGHTSTONE<br>ROOFING CO.</p>
  </div>

  <div class="divider"></div>

  <div class="person">
    <h1 class="person__name">REID <span class="accent">CALDER</span></h1>
    <p class="person__role">OWNER</p>
    <ul class="contacts">
      <li>
        <svg viewBox="0 0 24 24"><path d="M6.6 10.8a15.1 15.1 0 0 0 6.6 6.6l2.2-2.2c.3-.3.7-.4 1-.2 1.1.4 2.3.6 3.6.6.6 0 1 .4 1 1V20c0 .6-.4 1-1 1A17 17 0 0 1 3 4c0-.6.4-1 1-1h3.5c.6 0 1 .4 1 1 0 1.3.2 2.5.6 3.6.1.3 0 .7-.2 1z"/></svg>
        555-214-0387
      </li>
      <li>
        <svg viewBox="0 0 24 24"><path d="M2 5h20v14H2z" fill="none"/><path d="M2 5h20v2l-10 6L2 7zM2 9l10 6 10-6v10H2z"/></svg>
        reid@brightstoneroofing.co
      </li>
      <li>
        <svg viewBox="0 0 24 24"><path d="M12 2a10 10 0 1 0 0 20 10 10 0 0 0 0-20zm6.9 6h-3a15 15 0 0 0-1.3-3.8A8 8 0 0 1 18.9 8zM12 4c.9 1.2 1.5 2.6 1.9 4h-3.8c.4-1.4 1-2.8 1.9-4zM4.3 14a8 8 0 0 1 0-4h3.4a16 16 0 0 0 0 4zm.8 2h3a15 15 0 0 0 1.3 3.8A8 8 0 0 1 5.1 16zm3-8h-3a8 8 0 0 1 4.3-3.8A15 15 0 0 0 8.1 8zM12 20c-.9-1.2-1.5-2.6-1.9-4h3.8c-.4 1.4-1 2.8-1.9 4zm2.3-6H9.7a14 14 0 0 1 0-4h4.6a14 14 0 0 1 0 4zm.3 5.8a15 15 0 0 0 1.3-3.8h3a8 8 0 0 1-4.3 3.8zm1.7-5.8a16 16 0 0 0 0-4h3.4a8 8 0 0 1 0 4z"/></svg>
        www.brightstoneroofing.co
      </li>
    </ul>
  </div>
</section>

<section class="card card--back" aria-label="Business card back">
  <div class="mascot-area" role="img" aria-label="Brand mascot artwork in red and black"></div>

  <ul class="services">
    <li>residential &amp; commercial roofing</li>
    <li>Roof Repairs &amp; Maintenance</li>
    <li>Storm Damage &amp; Insurance Claims specialist</li>
    <li>Christmas Lights and permanent Christmas lights</li>
    <li class="pair"><span>Fencing</span><span>Windows</span><span>Gutters</span><span>Siding</span></li>
    <li class="pair"><span>Sheetrock</span><span>painting</span></li>
  </ul>

  <div class="brand">
    <p class="brand__name">BRIGHTSTONE<br>ROOFING CO.</p>
  </div>
</section>

</body>
</html>
```